Website Design and Build

This is a design and build of a dating site.

100% the most important thing is for the website to look good. I want this thing to be stunning and feel like a premium product so please only tender for the job if you excel at design and use of colours.

Theme is: premium, professional & uncluttered
Colour Scheme is: bright, fun and friendly but also reassuring and professional
 
Platforms: Initially just browser based (desktop and mobile) but if the proof of concept works we will roll it out to apps across the major platforms.

Marketing will be done primarily through organic online searches and content driven leads to a squeeze page, so SEO optimisation and experience with squeeze pages also a must.

Please include examples of sites you’ve done or other sites you think give a flavour of your vision for what this site will be. Any thoughts on palettes/colour scheme also useful.

I will provide the full brief to the successful designer.

Thank you for your time.

Industry/Entity Type

Dating

Coding

Coded - Design and coding required

Number of Pages Required

5+ page

Font styles to use
Sans Serif

Colors

Designer to choose colors to be used in the design.

Requirements
Must have
• Professional, Premium and uncluttered look.
• SEO optimisation.
• Squeeze page.
• A way to track different lead sources e.g. some of it will be content led to a squeeze page, some of it organic search engine hits, some of it unique referral links given to specific bloggers/influencers. I want to be able to track the success of all the different types of generating traffic to the site.
• I also want to be able to amend/update the site myself going forward so would like the spec/design to be clearly documented to allow me to do this.

```html
<!DOCTYPE html>
<html lang="en">
<head>
<meta charset="utf-8">
<title>Vellari Dating</title>
<link rel="stylesheet" href="https://fonts.googleapis.com/css2?family=Poppins:wght@400;500;600;700&family=Open+Sans:wght@400;600&display=swap">
<style>
:root{
  --magenta:#c2226a;
  --magenta-deep:#a3124f;
  --plum:#6b1f63;
  --ink:#1c1a1c;
  --text:#444;
  --light:#f1f1f1;
  --white:#fff;
  --head:'Poppins',sans-serif;
  --body:'Open Sans',sans-serif;
}
*{box-sizing:border-box;margin:0;padding:0}
html,body{width:1200px;height:3371px;overflow:hidden}
body{position:relative;background:var(--white);font-family:var(--body);color:var(--text)}
.abs{position:absolute}
.brand{font-family:var(--head);font-weight:600;color:var(--ink);font-size:34px;display:flex;align-items:center;gap:10px}
.brand .dot{width:30px;height:30px;border-radius:50%;background:var(--magenta)}

/* header */
.site-header{left:0;top:0;width:1200px;height:88px;background:var(--white);box-shadow:0 2px 6px rgba(0,0,0,.12);z-index:5}
.site-header .brand{position:absolute;left:132px;top:22px}
.main-nav{position:absolute;left:420px;top:33px;display:flex;gap:28px;font-family:var(--head);font-size:16px;color:var(--ink)}
.btn-signup{position:absolute;left:980px;top:27px;width:86px;height:32px;background:var(--magenta);color:var(--white);font-family:var(--head);font-size:13px;font-weight:500;display:flex;align-items:center;justify-content:center;border-radius:3px}

/* hero */
.hero-photo{left:0;top:88px;width:1200px;height:620px;
  background:
    radial-gradient(ellipse 260px 420px at 830px 300px,rgba(250,244,236,.75),rgba(250,244,236,0) 70%),
    radial-gradient(ellipse 500px 200px at 1050px 560px,rgba(214,150,90,.7),rgba(214,150,90,0) 70%),
    linear-gradient(180deg,#a9c6dc 0%,#dfe4e6 28%,#b7c3c6 40%,#8fa0a4 50%,#c7b8a4 60%,#d9ad7c 78%,#cf9863 100%)}
.hero-arrow{width:32px;height:32px;border-radius:50%;background:#3a3a3a;top:354px;display:flex;align-items:center;justify-content:center}
.signup-card{left:133px;top:184px;width:364px;height:362px;background:rgba(194,34,106,.93)}
.signup-card .card-title{height:66px;background:#3b3b3b;color:var(--white);font-family:var(--head);font-weight:600;font-size:25px;display:flex;align-items:center;justify-content:center}
.field-label{position:absolute;color:var(--white);font-size:13px}
.field{position:absolute;height:30px;background:var(--white);font-size:10px;color:#666;padding:0 8px;display:flex;align-items:center;justify-content:space-between}
.field.select::after{content:"";border:4px solid transparent;border-top-color:#444;margin-top:4px}
.btn-dark{position:absolute;background:#2d2d2d;color:var(--white);font-family:var(--head);font-size:13px;display:flex;align-items:center;justify-content:center}

/* welcome */
.welcome-frame{left:141px;top:806px;width:432px;height:290px;border:1px solid var(--magenta)}
.welcome-photo{left:133px;top:815px;width:432px;height:290px;
  background:
    radial-gradient(circle 60px at 230px 225px,#e8315a,rgba(232,49,90,0) 100%),
    radial-gradient(ellipse 170px 200px at 215px 210px,rgba(70,120,175,.85),rgba(70,120,175,0) 75%),
    radial-gradient(ellipse 90px 70px at 215px 70px,rgba(210,160,130,.8),rgba(210,160,130,0) 80%),
    linear-gradient(180deg,#c9d8e3,#b6c8d6)}
.section-title{font-family:var(--head);font-weight:600;color:var(--ink)}
.accent{color:var(--magenta)}
.welcome-title{left:612px;top:820px;font-size:34px}
.welcome-copy{left:612px;top:884px;width:462px;font-size:10.5px;line-height:25.5px;color:var(--text)}
.btn-outline{left:612px;top:1063px;width:110px;height:32px;border:1.5px solid var(--magenta);border-radius:16px;font-family:var(--head);font-size:11px;font-weight:500;color:var(--magenta-deep);display:flex;align-items:center;justify-content:center}

/* how it works */
.how-band{left:0;top:1250px;width:1200px;height:650px}
.how-title{left:0;width:1200px;top:1326px;text-align:center;color:var(--white);font-size:33px;font-weight:600;font-family:var(--head)}
.step{width:300px;text-align:center;top:1428px}
.step-ring{width:190px;height:190px;margin:0 auto;border:2px dashed rgba(255,255,255,.85);border-radius:50%;padding:8px}
.step-photo{width:100%;height:100%;border-radius:50%}
.step h3{margin-top:30px;font-family:var(--head);font-weight:500;font-size:18px;color:var(--white)}
.step p{margin-top:14px;font-size:11px;line-height:21px;color:#ddd}

/* features */
.feature-title{left:0;width:1200px;top:1952px;text-align:center;font-size:33px;line-height:46px;font-weight:600}
.feature{width:230px;text-align:center;top:2116px}
.feature-icon{display:block;margin:0 auto}
.feature h4{margin-top:20px;font-family:var(--head);font-weight:500;font-size:18px;color:var(--ink)}
.feature p{margin-top:8px;font-size:11px;line-height:22px;color:var(--text)}
.feature .more{margin-top:10px;font-family:var(--head);font-size:10px;color:#555;display:flex;justify-content:center;align-items:center;gap:4px}
.more i{width:10px;height:10px;border-radius:50%;background:#555;display:inline-block}

/* members */
.members-band{left:0;top:2455px;width:1200px;height:545px}
.members-title{left:0;width:1200px;top:2585px;text-align:center;color:var(--white);font-size:31px;font-weight:600;font-family:var(--head)}
.member{width:150px;text-align:center;top:2678px}
.member-photo{width:118px;height:118px;margin:0 auto;border-radius:50%;border:4px solid var(--white)}
.member p{margin-top:14px;font-size:12.5px;line-height:20px;color:var(--white)}

/* footer */
.site-footer{left:0;top:2985px;width:1200px;height:386px;background:var(--light)}
.footer-brand{left:130px;top:3088px}
.socials{left:152px;top:3166px;display:flex;gap:6px}
.socials span{width:28px;height:28px;border-radius:50%;border:1.5px solid var(--plum)}
.footer-head{font-family:var(--head);font-weight:600;font-size:18px;color:var(--ink)}
.footer-text{font-size:11px;line-height:20px;color:var(--text)}
.news-input{left:356px;top:3140px;width:228px;height:38px;background:var(--white);border:1px solid #ddd;font-size:11px;color:#444;padding:0 12px;display:flex;align-items:center}
.btn-sub{left:356px;top:3190px;width:110px;height:32px;background:var(--magenta);color:var(--white);font-family:var(--head);font-size:12px;font-weight:500;display:flex;align-items:center;justify-content:center}
.contact-row{display:flex;gap:12px;align-items:flex-start;font-size:12px;line-height:19px;color:var(--text)}
.quick-links{left:943px;top:3098px;list-style:none;font-size:11px;color:var(--text)}
.quick-links li{height:24px;display:flex;align-items:center;gap:12px}
.quick-links li::before{content:"›";font-size:14px;color:#555}
.copyright-bar{left:0;top:3300px;width:1200px;border-top:1px solid #ddd;height:71px;background:var(--white);display:flex;align-items:center;justify-content:center;font-size:12px;color:#444}
</style>
</head>
<body>

<header class="site-header abs">
  <div class="brand"><span class="dot"></span>Vellari</div>
  <nav class="main-nav"><span>Home</span><span>Top Members</span><span>About us</span><span>Membership</span><span>Contact Us</span></nav>
  <div class="btn-signup">SIGN UP</div>
</header>

<section>
  <div class="hero-photo abs" role="img" aria-label="Photo of a smiling couple walking along a sunny beach"></div>
  <div class="hero-arrow abs" style="left:62px"><svg width="10" height="12"><path d="M8 1 2 6l6 5" stroke="#fff" stroke-width="2" fill="none"/></svg></div>
  <div class="hero-arrow abs" style="left:1098px"><svg width="10" height="12"><path d="M2 1l6 5-6 5" stroke="#fff" stroke-width="2" fill="none"/></svg></div>
  <svg class="abs" style="left:0;top:600px" width="1200" height="120" viewBox="0 0 1200 120">
    <path d="M0 108 C200 40 400 40 650 65 C850 85 1050 70 1200 42 L1200 120 L0 120Z" fill="#fff"/>
    <path d="M0 100 C200 32 400 32 650 57 C850 77 1050 62 1200 34" stroke="#a3124f" stroke-width="7" fill="none"/>
    <path d="M0 90 C200 40 420 45 650 62" stroke="#c2226a" stroke-width="2" fill="none"/>
  </svg>

  <form class="signup-card abs">
    <div class="card-title">VELLARI DATING</div>
    <span class="field-label" style="left:20px;top:84px">I'm a :</span>
    <span class="field-label" style="left:188px;top:84px">looking for a :</span>
    <div class="field select" style="left:20px;top:112px;width:155px">Man</div>
    <div class="field select" style="left:188px;top:112px;width:155px">Woman</div>
    <span class="field-label" style="left:20px;top:152px">First name :</span>
    <div class="field" style="left:20px;top:178px;width:323px">Choose</div>
    <span class="field-label" style="left:20px;top:218px">D.O.B:</span>
    <div class="field select" style="left:20px;top:244px;width:97px">Day</div>
    <div class="field select" style="left:127px;top:244px;width:104px">Month</div>
    <div class="field select" style="left:241px;top:244px;width:102px">Year</div>
    <div class="btn-dark" style="left:20px;top:302px;width:128px;height:36px">SIGNING UP</div>
  </form>
</section>

<section>
  <div class="welcome-frame abs"></div>
  <div class="welcome-photo abs" role="img" aria-label="Photo of a happy couple holding a red paper heart"></div>
  <h1 class="section-title welcome-title abs">WELCOME TO <span class="accent">Vellari</span></h1>
  <p class="welcome-copy abs">Sed ut perspiciatis unde omnis iste natus error sit voluptatem accusantium doloremque laudantium, totam rem aperiam, eaque ipsa quae ab illo inventore veritatis et quasi architecto beatae vitae dicta sunt explicabo. Nemo enim ipsam voluptatem quia voluptas sit aspernatur aut odit aut fugit, sed quia consequuntur magni dolores eos qui ratione voluptatem sequi nesciunt. Neque porro quisquam est, qui dolorem ipsum quia dolor sit amet, consectetur, adipisci velit, sed quia non numquam</p>
  <div class="btn-outline abs">READ MORE</div>
</section>

<section>
  <svg class="how-band abs" viewBox="0 0 1200 650" role="img" aria-label="Dark backdrop photo of a couple at dusk">
    <defs>
      <linearGradient id="howBg" x1="0" x2="1"><stop offset="0" stop-color="#141213"/><stop offset=".6" stop-color="#1f1a1b"/><stop offset="1" stop-color="#2a2223"/></linearGradient>
      <radialGradient id="howGlow" cx=".78" cy=".55" r=".35"><stop offset="0" stop-color="#5a4640" stop-opacity=".75"/><stop offset="1" stop-color="#5a4640" stop-opacity="0"/></radialGradient>
      <radialGradient id="howGlow2" cx=".55" cy=".9" r=".3"><stop offset="0" stop-color="#4a3a35" stop-opacity=".6"/><stop offset="1" stop-color="#4a3a35" stop-opacity="0"/></radialGradient>
    </defs>
    <path d="M0 0H1200V645L0 590Z" fill="url(#howBg)"/>
    <path d="M0 0H1200V645L0 590Z" fill="url(#howGlow)"/>
    <path d="M0 0H1200V645L0 590Z" fill="url(#howGlow2)"/>
  </svg>
  <h2 class="how-title abs">HOW IT WORKS</h2>
  <div class="step abs" style="left:116px"><div class="step-ring"><div class="step-photo" role="img" aria-label="Photo of a hand holding a phone with a dating app" style="background:radial-gradient(circle 40px at 50% 45%,#e4566f,rgba(228,86,111,0) 100%),radial-gradient(ellipse 60% 70% at 55% 50%,#f2eded,rgba(242,237,237,0) 100%),linear-gradient(135deg,#d9c4bb,#a98a80)"></div></div><h3>Which Vellari Account?</h3><p>Sed ut perspiciatis unde omnis iste natus error sit voluptatem accusantium doloremque laudantium, totam rem aperiam, eaque ipsa quae</p></div>
  <div class="step abs" style="left:450px"><div class="step-ring"><div class="step-photo" role="img" aria-label="Photo of hands typing on a laptop" style="background:radial-gradient(ellipse 60% 40% at 55% 30%,#f1eee6,rgba(241,238,230,0) 100%),linear-gradient(160deg,#cfc9bc 0%,#8a857c 55%,#2e2b29 100%)"></div></div><h3>Vellari Dating</h3><p>Sed ut perspiciatis unde omnis iste natus error sit voluptatem accusantium doloremque laudantium, totam rem aperiam, eaque ipsa quae</p></div>
  <div class="step abs" style="left:784px"><div class="step-ring"><div class="step-photo" role="img" aria-label="Photo of a couple kissing outdoors" style="background:radial-gradient(ellipse 45% 55% at 60% 60%,#8a5f4c,rgba(138,95,76,0) 100%),radial-gradient(ellipse 40% 50% at 30% 70%,#3d5b82,rgba(61,91,130,0) 100%),linear-gradient(180deg,#c7d4de,#9fb0bf)"></div></div><h3>Vellari Hook-Ups</h3><p>Sed ut perspiciatis unde omnis iste natus error sit voluptatem accusantium doloremque laudantium, totam rem aperiam, eaque ipsa quae</p></div>
</section>

<section>
  <h2 class="section-title feature-title abs">What Makes <span class="accent">Vellari Match</span><br>Making So Practical?</h2>
  <svg width="0" height="0" style="position:absolute"><defs><linearGradient id="ringGrad" x1="0" y1="0" x2="1" y2="1"><stop offset="0" stop-color="#c2226a"/><stop offset="1" stop-color="#6b1f63"/></linearGradient></defs></svg>

  <div class="feature abs" style="left:110px">
    <svg class="feature-icon" width="104" height="104" viewBox="0 0 104 104" role="img" aria-label="Chat icon">
      <circle cx="52" cy="52" r="46" fill="none" stroke="url(#ringGrad)" stroke-width="7"/>
      <path d="M32 36h40a4 4 0 0 1 4 4v20a4 4 0 0 1-4 4H48l-10 8v-8h-6a4 4 0 0 1-4-4V40a4 4 0 0 1 4-4z" fill="#6b1f63"/>
      <circle cx="42" cy="50" r="3" fill="#fff"/><circle cx="52" cy="50" r="3" fill="#fff"/><circle cx="62" cy="50" r="3" fill="#fff"/>
    </svg>
    <h4>Quis autem vel eum</h4><p>Sed ut perspiciatis unde omnis iste natus error sit voluptatem accntium dolque laudantium, totam</p><div class="more">READ MORE <i></i></div></div>

  <div class="feature abs" style="left:360px">
    <svg class="feature-icon" width="104" height="104" viewBox="0 0 104 104" role="img" aria-label="Calendar icon">
      <circle cx="52" cy="52" r="46" fill="none" stroke="url(#ringGrad)" stroke-width="7"/>
      <rect x="32" y="34" width="40" height="38" rx="3" fill="none" stroke="#6b1f63" stroke-width="4"/>
      <path d="M32 44h40M42 29v10M62 29v10" stroke="#6b1f63" stroke-width="4"/>
      <path d="M39 52h6M49 52h6M59 52h6M39 61h6M49 61h6" stroke="#c2226a" stroke-width="4"/>
    </svg>
    <h4>Quis autem vel eum</h4><p>Sed ut perspiciatis unde omnis iste natus error sit voluptatem accntium dolque laudantium, totam</p><div class="more">READ MORE <i></i></div></div>

  <div class="feature abs" style="left:610px">
    <svg class="feature-icon" width="104" height="104" viewBox="0 0 104 104" role="img" aria-label="Checklist icon">
      <circle cx="52" cy="52" r="46" fill="none" stroke="url(#ringGrad)" stroke-width="7"/>
      <rect x="36" y="30" width="32" height="44" rx="3" fill="none" stroke="#6b1f63" stroke-width="4"/>
      <path d="M41 42l3 3 5-6M41 54l3 3 5-6M41 66l3 3 5-6" stroke="#c2226a" stroke-width="3" fill="none"/>
      <path d="M53 43h10M53 55h10M53 67h10" stroke="#6b1f63" stroke-width="3"/>
    </svg>
    <h4>Quis autem vel eum</h4><p>Sed ut perspiciatis unde omnis iste natus error sit voluptatem accntium dolque laudantium, totam</p><div class="more">READ MORE <i></i></div></div>

  <div class="feature abs" style="left:860px">
    <svg class="feature-icon" width="104" height="104" viewBox="0 0 104 104" role="img" aria-label="Star icon">
      <circle cx="52" cy="52" r="46" fill="none" stroke="url(#ringGrad)" stroke-width="7"/>
      <path d="M52 30l6.5 13.5 14.5 2-10.5 10 2.5 14.5L52 63l-13 7 2.5-14.5-10.5-10 14.5-2z" fill="#6b1f63"/>
    </svg>
    <h4>Quis autem vel eum</h4><p>Sed ut perspiciatis unde omnis iste natus error sit voluptatem accntium dolque laudantium, totam</p><div class="more">READ MORE <i></i></div></div>
</section>

<section>
  <svg class="members-band abs" viewBox="0 0 1200 545" role="img" aria-label="Magenta-tinted backdrop photo of a couple">
    <defs>
      <linearGradient id="memBg" x1="0" x2="1" y1="0" y2="1"><stop offset="0" stop-color="#b01a60"/><stop offset=".5" stop-color="#c8337a"/><stop offset="1" stop-color="#b0205f"/></linearGradient>
      <radialGradient id="memGlow" cx=".35" cy=".75" r=".35"><stop offset="0" stop-color="#e06a9c" stop-opacity=".55"/><stop offset="1" stop-color="#e06a9c" stop-opacity="0"/></radialGradient>
      <radialGradient id="memGlow2" cx=".8" cy=".3" r=".3"><stop offset="0" stop-color="#8e1550" stop-opacity=".5"/><stop offset="1" stop-color="#8e1550" stop-opacity="0"/></radialGradient>
    </defs>
    <path d="M0 45L1200 0V470C1000 520 800 540 600 510C400 480 200 470 0 510Z" fill="url(#memBg)"/>
    <path d="M0 45L1200 0V470C1000 520 800 540 600 510C400 480 200 470 0 510Z" fill="url(#memGlow)"/>
    <path d="M0 45L1200 0V470C1000 520 800 540 600 510C400 480 200 470 0 510Z" fill="url(#memGlow2)"/>
    <path d="M0 510C200 470 400 480 600 510C800 540 1000 520 1200 470" stroke="#6b1f63" stroke-width="6" fill="none"/>
  </svg>
  <h2 class="members-title abs">TOP MEMBERS</h2>
  <div class="member abs" style="left:116px"><div class="member-photo" role="img" aria-label="Member portrait photo" style="background:radial-gradient(ellipse 45% 50% at 55% 50%,#e9bfa8,rgba(233,191,168,0) 100%),linear-gradient(160deg,#8a4a36,#c98f78 60%,#e3d0c4)"></div><p>Quis autem vel<br>Vellari</p></div>
  <div class="member abs" style="left:279px"><div class="member-photo" role="img" aria-label="Member portrait photo" style="background:radial-gradient(ellipse 45% 50% at 50% 45%,#e3b79c,rgba(227,183,156,0) 100%),linear-gradient(180deg,#f0ece6,#cfd6dd)"></div><p>Quis autem vel<br>Vellari</p></div>
  <div class="member abs" style="left:442px"><div class="member-photo" role="img" aria-label="Member portrait photo" style="background:radial-gradient(ellipse 35% 40% at 50% 45%,#e2b49a,rgba(226,180,154,0) 100%),linear-gradient(180deg,#3a2a26,#6d4a3e)"></div><p>Quis autem vel<br>Vellari</p></div>
  <div class="member abs" style="left:606px"><div class="member-photo" role="img" aria-label="Member portrait photo" style="background:radial-gradient(ellipse 40% 45% at 50% 45%,#efc2a4,rgba(239,194,164,0) 100%),linear-gradient(160deg,#e08a3a,#c45a2a 60%,#7a3a22)"></div><p>Quis autem vel<br>Vellari</p></div>
  <div class="member abs" style="left:770px"><div class="member-photo" role="img" aria-label="Member couple photo" style="background:radial-gradient(ellipse 50% 45% at 50% 45%,#c99884,rgba(201,152,132,0) 100%),linear-gradient(180deg,#5a4a46,#2f2a2a)"></div><p>Quis autem vel<br>Vellari</p></div>
  <div class="member abs" style="left:934px"><div class="member-photo" role="img" aria-label="Member portrait photo" style="background:radial-gradient(ellipse 35% 45% at 50% 45%,#e6c0a8,rgba(230,192,168,0) 100%),linear-gradient(180deg,#b9aaa4,#5a3f36)"></div><p>Quis autem vel<br>Vellari</p></div>
</section>

<footer>
  <div class="site-footer abs" style="z-index:-1"></div>
  <div class="brand footer-brand abs"><span class="dot"></span>Vellari</div>
  <div class="socials abs"><span></span><span></span><span></span><span></span></div>

  <h3 class="footer-head abs" style="left:356px;top:3050px">SIGN UP FOR NEWSLETTER</h3>
  <p class="footer-text abs" style="left:356px;top:3093px;width:230px">Excepteur sint occaecat cupidatat non proident, sunt in culpa qui officia deserunt</p>
  <div class="news-input abs">Enter email</div>
  <div class="btn-sub abs">SUBSCRIPTION</div>

  <h3 class="footer-head abs" style="left:681px;top:3050px">CONTACT US</h3>
  <div class="contact-row abs" style="left:681px;top:3100px"><svg width="12" height="16" viewBox="0 0 12 16"><path d="M6 0a6 6 0 0 1 6 6c0 4-6 10-6 10S0 10 0 6a6 6 0 0 1 6-6z" fill="#333"/><circle cx="6" cy="6" r="2.2" fill="#f1f1f1"/></svg><span>Vellari<br>14 Linden Row London N4</span></div>
  <div class="contact-row abs" style="left:681px;top:3155px"><svg width="12" height="14" viewBox="0 0 24 24"><path d="M6.6 10.8a15 15 0 0 0 6.6 6.6l2.2-2.2a1 1 0 0 1 1-.2 11 11 0 0 0 3.6.6 1 1 0 0 1 1 1V20a1 1 0 0 1-1 1A17 17 0 0 1 3 4a1 1 0 0 1 1-1h3.5a1 1 0 0 1 1 1 11 11 0 0 0 .6 3.6 1 1 0 0 1-.3 1z" fill="#333"/></svg><span>Phone: 1300 555 014</span></div>
  <div class="contact-row abs" style="left:681px;top:3182px"><svg width="12" height="12" viewBox="0 0 12 10"><rect width="12" height="10" fill="#333"/><path d="M0 0l6 5 6-5" stroke="#f1f1f1" fill="none"/></svg><span>info@vellari.com</span></div>

  <h3 class="footer-head abs" style="left:943px;top:3056px">QUICK LINKS</h3>
  <ul class="quick-links abs"><li>Home</li><li>Top Members</li><li>About us</li><li>Membership</li><li>Contact Us</li></ul>

  <div class="copyright-bar abs">© Copyright Vellari 2018. All rights reserved</div>
</footer>

</body>
</html>
```